Tobin's Jewelry Studio Needs a Moving Location Flyer

We need a flyer to inform our customers of our location moving. We will be moving to our city's downtown which is only 1 mile away from our current address. We will be having a moving sale ( Up to 80% off). The sale starts Sept. 8th Our business creates, sells, and repairs fine jewelry. Dimensions are 5"x8"

Target Market(s)

Women ages 25-55

Industry/Entity Type

Jewelry

Colors
85abd2
cfdeed

Requirements
Must have
• Our logo
• Mention of the sale
• Our current address
• 4785 Cresthaven Blvd.
• Dunmore, Ca 94318
• (415)826-3319
Nice to have
• Mention that we're relocating to downtown Dunmore (new location opening Nov. 1st.)

```html
<!DOCTYPE html>
<html lang="en">
<head>
<meta charset="UTF-8">
<title>Tobin's Jewelry Studio – Moving Sale Flyer</title>
<link href="https://fonts.googleapis.com/css2?family=Great+Vibes&family=Pinyon+Script&family=Fredoka:wght@600;700&family=Open+Sans:ital,wght@0,600;1,700&display=swap" rel="stylesheet">
<style>
  :root {
    --page-bg: #e9e6e1;
    --blue-deep: #1b2d4e;
    --blue-mid: #3f6498;
    --blue-light: #85abd2;
    --blue-pale: #cfdeed;
    --navy-ink: #0f1834;
    --gold: #e8b53c;
    --white: #ffffff;
    --footer: #262626;
  }
  * { margin: 0; padding: 0; box-sizing: border-box; }
  html, body { width: 1200px; height: 1200px; overflow: hidden; }
  body { background: var(--page-bg); position: relative; }

  .flyer {
    position: absolute; left: 254px; top: 53px; width: 694px; height: 1110px;
    background: radial-gradient(ellipse at 45% 62%, #7ea2cf 0%, #5479ad 35%, #3a5d91 70%, #2a4675 100%);
    overflow: hidden;
    box-shadow: 0 6px 18px rgba(0,0,0,.25);
  }
  .portrait-art {
    position: absolute; left: 0; top: 185px; width: 546px; height: 826px;
    background: radial-gradient(ellipse at 40% 35%, rgba(150,180,215,.35), rgba(60,95,145,0) 70%);
  }
  .pattern-strip {
    position: absolute; right: 0; top: 185px; width: 148px; height: 826px;
    background: linear-gradient(180deg, #2f4e80, #284471);
    opacity: .85;
  }
  .top-strip { position: absolute; left: 0; top: 0; width: 100%; height: 29px; background: #2a4878; }
  .header {
    position: absolute; left: 0; top: 29px; width: 100%; height: 156px;
    background: var(--blue-deep);
    display: flex; align-items: center; justify-content: center; gap: 18px;
  }
  .header-rule { position: absolute; top: 77px; height: 3px; width: 100%; background: #4a2a1c; opacity: .8; }
  .brand {
    position: relative; display: flex; align-items: center; gap: 16px;
    background: var(--blue-deep); padding: 0 22px;
  }
  .brand-dot { width: 54px; height: 54px; border-radius: 50%; background: var(--blue-pale); }
  .brand-name {
    font-family: 'Open Sans', sans-serif; font-weight: 600; font-size: 34px;
    color: var(--blue-pale); letter-spacing: .5px;
  }

  .sale-title {
    position: absolute; left: 264px; top: 202px; width: 167px; height: 45px;
    border-top: 2px solid var(--gold); border-bottom: 2px solid var(--gold);
    font-family: 'Great Vibes', cursive; color: var(--gold); font-size: 36px;
    display: flex; align-items: center; justify-content: center; white-space: nowrap;
  }
  .discount-stamp { position: absolute; left: 219px; top: 261px; width: 264px; height: 264px; }
  .stamp-text {
    position: absolute; left: 219px; width: 264px; text-align: center;
    font-family: 'Great Vibes', cursive; color: var(--white);
  }
  .stamp-upto { top: 290px; font-size: 44px; }
  .stamp-pct { top: 358px; font-size: 64px; }
  .stamp-off { top: 432px; font-size: 40px; }

  .sale-date {
    position: absolute; left: 0; top: 530px; width: 100%; padding-right: 40px;
    text-align: center; font-family: 'Great Vibes', cursive; color: var(--white);
  }
  .sale-date small { font-size: 34px; }
  .sale-date span { font-size: 72px; }

  .address-label {
    position: absolute; left: 0; top: 608px; width: 100%; padding-right: 44px; text-align: center;
    font-family: 'Pinyon Script', cursive; font-size: 30px; color: var(--navy-ink);
  }
  .contact {
    position: absolute; left: 124px; top: 652px;
    font-family: 'Fredoka', sans-serif; font-weight: 700; color: var(--navy-ink);
    font-size: 37px; line-height: 46px; text-transform: uppercase;
  }
  .contact-line { display: flex; align-items: center; gap: 8px; }
  .contact-line.indent { padding-left: 30px; }
  .contact-line.phone { padding-left: 20px; color: var(--white); }
  .icon { flex: none; }

  .ring-photo {
    position: absolute; left: 275px; top: 802px; width: 160px; height: 170px;
    border-radius: 50% 50% 46% 46%;
    background: radial-gradient(circle at 50% 45%, #c8662e 0%, #8a5a22 30%, #c9b06a 55%, #4a3a1e 80%, rgba(40,60,95,0) 100%);
  }

  .footer {
    position: absolute; left: 0; bottom: 0; width: 100%; height: 99px;
    background: var(--footer); color: var(--white); text-align: center;
    padding-top: 12px;
  }
  .footer-main { font-family: 'Pinyon Script', cursive; font-size: 28px; line-height: 40px; }
  .footer-main strong { font-family: 'Open Sans', sans-serif; font-style: italic; font-weight: 700; font-size: 30px; }
  .footer-sub { font-family: 'Pinyon Script', cursive; font-size: 26px; line-height: 38px; }
</style>
</head>
<body>
  <main class="flyer">
    <div class="portrait-art" role="img" aria-label="Faded vintage portrait of a woman in profile, tinted blue"></div>
    <div class="pattern-strip" role="img" aria-label="Decorative lace and paisley pattern strip in dark blue"></div>

    <div class="top-strip"></div>
    <header class="header">
      <div class="header-rule"></div>
      <div class="brand">
        <div class="brand-dot"></div>
        <span class="brand-name">Tobin's Jewelry Studio</span>
      </div>
    </header>

    <div class="sale-title">Moving sale</div>

    <svg class="discount-stamp" viewBox="0 0 264 264" aria-hidden="true">
      <circle cx="132" cy="132" r="126" fill="none" stroke="#ffffff" stroke-width="6"/>
      <circle cx="132" cy="132" r="112" fill="none" stroke="#ffffff" stroke-width="2"/>
    </svg>
    <div class="stamp-text stamp-upto">Upto</div>
    <div class="stamp-text stamp-pct">80 %</div>
    <div class="stamp-text stamp-off">OFF.</div>

    <div class="sale-date"><small>From </small><span>Sept. 8th</span></div>

    <div class="address-label">Our current address:</div>
    <address class="contact" style="font-style:normal">
      <div class="contact-line">
        <svg class="icon" width="24" height="32" viewBox="0 0 24 32" aria-hidden="true">
          <path d="M12 2C6.5 2 2 6.3 2 11.7 2 19 12 30 12 30s10-11 10-18.3C22 6.3 17.5 2 12 2z" fill="none" stroke="#0f1834" stroke-width="3.5"/>
          <circle cx="12" cy="11.5" r="3.5" fill="#0f1834"/>
        </svg>
        4785 Cresthaven Blvd.
      </div>
      <div class="contact-line indent">Dunmore, Ca 94318</div>
      <div class="contact-line phone">
        <svg class="icon" width="42" height="32" viewBox="0 0 42 32" aria-hidden="true">
          <rect x="1" y="2" width="9" height="28" rx="3" fill="#0f1834"/>
          <rect x="12" y="4" width="29" height="26" rx="3" fill="#0f1834"/>
          <g fill="#cfdeed">
            <rect x="17" y="9" width="4" height="4"/><rect x="24" y="9" width="4" height="4"/><rect x="31" y="9" width="4" height="4"/>
            <rect x="17" y="16" width="4" height="4"/><rect x="24" y="16" width="4" height="4"/><rect x="31" y="16" width="4" height="4"/>
            <rect x="17" y="23" width="4" height="4"/><rect x="24" y="23" width="4" height="4"/><rect x="31" y="23" width="4" height="4"/>
          </g>
        </svg>
        (415)826-3319
      </div>
    </address>

    <div class="ring-photo" role="img" aria-label="Photo of a gold cocktail ring with an orange center stone ringed by crystals"></div>

    <footer class="footer">
      <p class="footer-main">We're relocating to <strong>Downtown Dunmore</strong></p>
      <p class="footer-sub">(new location opening Nov. 1st.)</p>
    </footer>
  </main>
</body>
</html>
```